Business Card Design Project

Need a business card with logo that is attached.
Company name: Tolmen Brisk Solutions, LLC
My name: Lorna Tolmen
Title: President
Phone number: 703-555-0148
Email: ltolmen@tolmenbrisksolutions.example
web site: www.tolmenbrisksolutions.example

Industry/Entity Type

Business

```html
<!DOCTYPE html>
<html lang="en">
<head>
<meta charset="utf-8">
<title>Tolmen Brisk Solutions – Business Card</title>
<link rel="stylesheet" href="https://fonts.googleapis.com/css2?family=Tinos:wght@400;700&display=swap">
<style>
  :root {
    --page: #ffffff;
    --card: #353b3c;
    --ink: #c9f3e6;
    --ink-muted: #8fb6b3;
    --band-start: #1d45a6;
    --band-end: #3f8f96;
    --mark-blue: #2a6fd0;
    --mark-text: #3f7fd6;
  }
  * { margin: 0; padding: 0; box-sizing: border-box; }
  html, body {
    width: 1200px;
    height: 1000px;
    overflow: hidden;
    background: var(--page);
  }
  .canvas {
    position: relative;
    width: 1200px;
    height: 1000px;
  }
  .card {
    position: absolute;
    left: 75px;
    top: 182px;
    width: 1053px;
    height: 636px;
    background: var(--card);
    font-family: "Tinos", "Times New Roman", serif;
    font-weight: 700;
    color: var(--ink);
  }
  .card-bands {
    position: absolute;
    inset: 0;
  }
  .company-name {
    position: absolute;
    left: 17px;
    top: 32px;
    font-size: 45px;
    line-height: 1;
    white-space: nowrap;
  }
  .holder {
    position: absolute;
    left: 420px;
    width: 530px;
    text-align: center;
    line-height: 1;
    white-space: nowrap;
  }
  .holder-name { top: 208px; font-size: 68px; }
  .holder-title { top: 340px; font-size: 44px; left: 448px; }
  .contact {
    position: absolute;
    left: 38px;
    top: 506px;
    font-size: 29px;
    line-height: 40px;
    list-style: none;
    white-space: nowrap;
  }
  .contact-web { color: var(--ink-muted); }
  .brand-mark {
    position: absolute;
    left: 708px;
    top: 510px;
    display: flex;
    align-items: center;
    gap: 18px;
  }
  .brand-dot {
    width: 96px;
    height: 96px;
    border-radius: 50%;
    background: var(--mark-blue);
  }
  .brand-name {
    font-size: 25px;
    line-height: 29px;
    color: var(--mark-text);
    font-weight: 400;
    text-transform: uppercase;
    letter-spacing: 0.5px;
  }
</style>
</head>
<body>
<div class="canvas">
  <section class="card">
    <svg class="card-bands" width="1053" height="636" viewBox="0 0 1053 636" aria-hidden="true">
      <defs>
        <linearGradient id="band" x1="0" y1="0" x2="1" y2="0">
          <stop offset="0" stop-color="var(--band-start)"/>
          <stop offset="1" stop-color="var(--band-end)"/>
        </linearGradient>
        <linearGradient id="underline" x1="0" y1="0" x2="0" y2="1">
          <stop offset="0" stop-color="#4f7fd0"/>
          <stop offset="1" stop-color="#1d3f96"/>
        </linearGradient>
      </defs>
      <rect class="title-underline" x="0" y="74" width="576" height="14" fill="url(#underline)"/>
      <rect class="divider" x="0" y="114" width="1053" height="12" fill="url(#band)"/>
      <rect class="divider" x="0" y="466" width="1053" height="13" fill="url(#band)"/>
    </svg>

    <h1 class="company-name">Tolmen Brisk Solutions, LLC</h1>
    <h2 class="holder holder-name">Lorna Tolmen</h2>
    <p class="holder holder-title">President</p>

    <ul class="contact">
      <li class="contact-phone">Phone number: 703-555-0148</li>
      <li class="contact-email">Email: ltolmen@tolmenbrisksolutions.example</li>
      <li class="contact-web">www.tolmenbrisksolutions.example</li>
    </ul>

    <div class="brand-mark">
      <span class="brand-dot" aria-hidden="true"></span>
      <p class="brand-name">Tolmen Brisk<br>Solutions<br>LLC</p>
    </div>
  </section>
</div>
</body>
</html>
```